Shop Window Signs and Fence Designs

Hi guys im looking for creativity people in helping me with these designs 50 all up

Designs on various signage displays for shop windows and store fronts.

50 separate designs with on going work available.
Each design to be suppled in PDF

20 - Vertical designs - (posters)
20 - Horizontal designs - (banners) for hanging on fences e.g.
5 - Vertical - sales, garage sale EG
5 - Horizontal - sales, garage sale EG

MIX THINGS UP GUYS these are my samples below

At this stage only looking at straight eges designs.

COLOUR FULL DESIGNS EYE CATCHING
thanks guys lots more work to come for the right designer

Target Market(s)

Customers - Shoppers

Industry/Entity Type

Shop

Font styles to use
Serif
Sans Serif
Decorative
Script

Colors

Designer to choose colors to be used in the design.

Requirements
Must have
• POSTERS - in VERTICAL format
• 1900 x 1320 200gsm
• 2600 x 1600 200gsm
• 1540 x 1060 250gsm
• 2440 x1320 200gsm
• BANNERS - in HORIZONTAL format
• 1000 x 5000
• 1000 x 4000
• 1000 x 3000
• 1000 x 2000
Nice to have
• Be creative
Should not have
• Be creative

```html
<!DOCTYPE html>
<html lang="en">
<head>
<meta charset="utf-8">
<title>Summer Sale Signs</title>
<link rel="stylesheet" href="https://fonts.googleapis.com/css2?family=Jost:ital,wght@0,200;0,300;0,600;0,700;1,300;1,600;1,700&display=swap">
<style>
  :root {
    --sign-yellow: #fff200;
    --ink: #000000;
    --paper: #ffffff;
  }
  html, body {
    margin: 0;
    padding: 0;
    width: 1200px;
    height: 825px;
    overflow: hidden;
    background: var(--paper);
  }
  .sign-sheet {
    display: block;
    width: 1200px;
    height: 825px;
  }
  .sign-bg { fill: var(--sign-yellow); }
  .ink { fill: var(--ink); font-family: "Jost", sans-serif; }
  .title-thin { font-weight: 200; font-size: 62px; letter-spacing: 9px; }
  .label-bold { font-weight: 700; font-size: 38px; letter-spacing: 9px; }
  .figure-big { font-weight: 600; font-size: 205px; }
  .discount-frame { fill: none; stroke: var(--ink); stroke-width: 2; }
  .badge-sale { font-weight: 300; font-style: italic; font-size: 70px; letter-spacing: 8px; }
  .badge-figure { font-weight: 600; font-style: italic; font-size: 200px; }
  .badge-note { font-weight: 700; font-style: italic; font-size: 52px; letter-spacing: 1px; }
</style>
</head>
<body>
<svg class="sign-sheet" viewBox="0 0 1200 825" xmlns="http://www.w3.org/2000/svg">
  <g class="poster-summer-sale">
    <rect class="sign-bg" x="55" y="35" width="520" height="748"/>
    <text class="ink title-thin" x="303" y="165" text-anchor="middle" textLength="370" lengthAdjust="spacing">SUMMER</text>
    <text class="ink title-thin" x="303" y="250" text-anchor="middle" textLength="210" lengthAdjust="spacing">SALE</text>
    <text class="ink label-bold" x="180" y="362" textLength="153" lengthAdjust="spacing">UP TO</text>
    <rect class="discount-frame" x="177" y="376" width="276" height="275"/>
    <text class="ink figure-big" x="100" y="595" textLength="425" lengthAdjust="spacing">50%</text>
    <text class="ink label-bold" x="355" y="697" textLength="95" lengthAdjust="spacing">OFF</text>
  </g>
  <g class="badge-all-items">
    <circle class="sign-bg" cx="880" cy="380" r="278"/>
    <text class="ink badge-sale" x="875" y="250" text-anchor="middle" textLength="220" lengthAdjust="spacing">SALE</text>
    <text class="ink badge-figure" x="698" y="460" textLength="392" lengthAdjust="spacing">70%</text>
    <text class="ink badge-note" x="752" y="557" textLength="256" lengthAdjust="spacing">ALL ITEM</text>
  </g>
</svg>
</body>
</html>
```